Australian new start up company needs a Logo & Web Design

We need a smart, simple logo and web design for a new start up company based in Melbourne Australia called "Tidewater Enterprise Assist". The logo is to be used on all marketing materials. The website is the primary interface of the company.

Our initial phase (launch) will provide a B2B directory service, resources and solutions.
A.) By listing on our site, small businesses can generate sales for their business. Regardless of where they might be located in the world, then can sell to Australian small businesses.
B.)Through our resource centre, small businesses can find practical and up to date resources for their business in pre-start up, start up, growth, maintenance and succession planning or exit stage.
C.)And on our site, we'll offer time and money saving solutions. These solutions can be packaged solutions (ie. Car Branding = including design, print and application onto the vehicle at a discounted price). Customers can also contact us if they want to advertise their business solution.

Eventually, there will be a total of five services inclusive of the directory described above (ie. business classifieds, link to Asian businesses, expos/seminars listing, etc). We hope to see this site grow over the next 18 months. All services will be aimed at servicing small businesses. Individuals through to large businesses located any where in the world can service these small businesses.

We would like to see designs that are professional. They should communicate growth, trust, professionalism and forward thinking.

Target Market(s)

Small Businesses (ie. employ up to 150 employees)

Industry/Entity Type

Business

Requirements
Must have
• We have attached some of the current files that we have designed ourselves. We feel that our material is lacking in appeal, professionalism and consistency. However, it does give a good idea of the requirements needed such as login, directory on the frontpage, etc. The wording is not final, as we are trying to finalise the design first. The logo was simply a placeholder as that definitely needs to be designed.

We want a logo and website that sticks in people's minds, its memorable.

We want a website that is EASY to use and navigate.
Nice to have
• Eventually, there will be a total of five services inclusive of the directory described above (ie. business classifieds, Asian businesses, expos/seminars listing, etc). They are very different types of services. The common thread is that all services will be aimed at servicing small businesses.

The winning design will need to help us to visualize how their design suits our future growth.

```html
<!DOCTYPE html>
<html lang="en">
<head>
<meta charset="utf-8">
<title>Tidewater Enterprise Assist</title>
<link rel="stylesheet" href="https://fonts.googleapis.com/css2?family=Open+Sans:ital,wght@0,400;0,600;1,400&family=Crimson+Text&display=swap">
<style>
:root{
  --slate:#6b8799;
  --slate-dark:#4f6f87;
  --slate-light:#9fb3c2;
  --navy:#3c5676;
  --ink:#2f3a44;
  --label:#8c99a4;
  --strip:#8a9fb3;
  --white:#ffffff;
  --nav-top:#f4f7f8;
  --nav-bottom:#dfe7eb;
}
*{box-sizing:border-box;margin:0;padding:0}
html,body{width:1200px;height:900px;overflow:hidden;background:var(--white)}
body{position:relative;font-family:"Open Sans",Arial,sans-serif;color:var(--ink)}
.abs{position:absolute}

/* header */
.brand{left:186px;top:10px;width:240px;height:100px}
.brand-mark{left:80px;top:0;width:58px;height:58px;background:var(--slate);}
.brand-name{left:0;top:70px;font-family:"Crimson Text",Georgia,serif;font-size:21px;color:var(--slate);white-space:nowrap}

.login-label{font-style:italic;font-size:15px;color:var(--label)}
.login-field{width:129px;height:25px;border:1px solid #c8d0d6;border-radius:4px;background:var(--white);box-shadow:inset 0 1px 2px rgba(0,0,0,.08)}
.forgot{left:691px;top:65px;font-size:10px;color:var(--navy)}
.login-btn{left:899px;top:71px;width:63px;height:16px;border-radius:3px;background:linear-gradient(#f2f2f2,#c9cdd0);font-size:12px;font-style:italic;color:var(--label);text-align:center;line-height:15px;box-shadow:0 1px 1px rgba(0,0,0,.2)}

.nav{left:186px;top:119px;width:828px;height:41px;background:linear-gradient(var(--nav-top),var(--nav-bottom));display:flex;align-items:center}
.nav-item{font-size:16px;color:var(--ink);text-align:center;height:41px;line-height:41px}
.nav-item.is-active{background:var(--slate-dark);color:var(--white);border-top:3px solid var(--slate-light);line-height:37px}

/* hero */
.hero-band{left:0;top:160px;width:1200px;height:339px;background:var(--slate);border-top:2px solid #5b788b;border-bottom:2px solid #5b788b}
.hero-photo{left:191px;top:177px;width:818px;height:305px;background:linear-gradient(100deg,#c9d1d8 0%,#e6e9ec 35%,#b9c1c9 60%,#4a4f57 100%);box-shadow:0 2px 8px rgba(0,0,0,.45)}
.hero-copy{left:196px;top:329px;width:378px;height:146px;background:rgba(110,130,150,.55);border:1px solid rgba(255,255,255,.35);color:var(--white);font-size:15px;line-height:21px;text-align:center;padding-top:14px}
.learn-more{left:783px;top:418px;width:212px;height:52px;background:linear-gradient(#6f8ba0 0 55%,#4f6f87 55%);border:1px solid rgba(255,255,255,.4);color:var(--white);font-weight:600;font-size:23px;letter-spacing:1px;text-align:center;line-height:52px}
.hero-arrow{top:304px}

/* packages */
.card{top:510px;width:204px;height:223px;border:1px solid var(--slate-light);background:linear-gradient(135deg,#f7f9fa,#e3eaee);overflow:hidden}
.card-title{height:40px;background:linear-gradient(#8aa2b3,#5f7d91);color:var(--white);font-size:19px;text-align:center;line-height:38px}
.card-price{position:absolute;left:7px;top:44px;font-size:23px;color:var(--navy);letter-spacing:.5px}
.card-list{position:absolute;left:17px;top:98px;list-style:none;font-size:13.5px;line-height:19px;color:var(--navy);letter-spacing:.8px}
.card-list li::before{content:"•"}
.card-corner{position:absolute;right:0;bottom:0}
.card-go{position:absolute;right:6px;bottom:4px;color:var(--white);font-size:28px;letter-spacing:2px}

/* footer */
.footer{left:0;top:768px;width:1200px;height:100px;background:var(--slate);border-top:2px solid #86a0b1}
.footer-link{font-size:14px;color:var(--white)}
.social{top:788px;width:28px;height:28px;border-radius:3px;background:linear-gradient(#6f9ad0,#3f6fb0);box-shadow:2px 2px 3px rgba(0,0,0,.3)}
.legal{left:0;top:870px;width:1200px;height:30px;background:var(--strip);color:#dfe6ec;font-size:7px;text-align:center;line-height:30px}
</style>
</head>
<body>

<header>
  <div class="abs brand">
    <div class="abs brand-mark"></div>
    <div class="abs brand-name">Tidewater Enterprise Assist</div>
  </div>

  <div class="abs login-label" style="left:691px;top:19px">Username:</div>
  <div class="abs login-field" style="left:691px;top:39px"></div>
  <div class="abs login-label" style="left:840px;top:19px">Password:</div>
  <div class="abs login-field" style="left:840px;top:39px"></div>
  <div class="abs forgot">Forgot your password?</div>
  <div class="abs login-btn">Login</div>

  <nav class="abs nav">
    <div class="nav-item is-active" style="width:90px">HOME</div>
    <div class="nav-item" style="width:144px">ABOUT US</div>
    <div class="nav-item" style="width:142px">WHAT WE DO</div>
    <div class="nav-item" style="width:166px">HOW WE WORK</div>
    <div class="nav-item" style="width:142px">CONTACT</div>
    <div class="nav-item" style="width:110px">CAREERS</div>
  </nav>
</header>

<section>
  <div class="abs hero-band"></div>
  <svg class="abs hero-arrow" style="left:154px" width="20" height="26" viewBox="0 0 20 26"><path d="M15 2 L5 13 L15 24" fill="none" stroke="#fff" stroke-width="3.5"/></svg>
  <svg class="abs hero-arrow" style="left:1023px" width="20" height="26" viewBox="0 0 20 26"><path d="M5 2 L15 13 L5 24" fill="none" stroke="#fff" stroke-width="3.5"/></svg>
  <div class="abs hero-photo" role="img" aria-label="Photo of four smiling business people in suits shaking hands in an office"></div>
  <div class="abs hero-copy">
    Online directory, dedicated to servicing Australian<br>Small Businesses<br>Advertise for as little as $2/month<br>Generate sales, increase brand awareness<br>Limited time business offers<br>Small Business resource centre
  </div>
  <div class="abs learn-more">LEARN MORE</div>
</section>

<section>
  <div class="abs card" style="left:183px">
    <div class="card-title">Start-Up Package</div>
    <div class="card-price">$2000</div>
    <ul class="card-list"><li>Logo Design</li><li>Website Design</li><li>Stationery</li><li>Directory Listing</li></ul>
    <svg class="card-corner" width="96" height="82"><polygon points="96,0 96,82 0,82" fill="#6b8799"/></svg>
    <div class="card-go">GO</div>
  </div>
  <div class="abs card" style="left:393px">
    <div class="card-title">Biz Growth Package</div>
    <div class="card-price">$1000</div>
    <ul class="card-list"><li>xxxx</li><li>xxxx</li><li>xxxx</li><li>Directory Listing</li></ul>
    <svg class="card-corner" width="96" height="82"><polygon points="96,0 96,82 0,82" fill="#6b8799"/></svg>
    <div class="card-go">GO</div>
  </div>
  <div class="abs card" style="left:602px">
    <div class="card-title">Biz Coaching</div>
    <div class="card-price">$2500</div>
    <ul class="card-list"><li>xx hours of</li><li>Business Coaching</li><li>Directory Listing</li></ul>
    <svg class="card-corner" width="96" height="82"><polygon points="96,0 96,82 0,82" fill="#6b8799"/></svg>
    <div class="card-go">GO</div>
  </div>
  <div class="abs card" style="left:811px">
    <div class="card-title">Vehicle Advertising</div>
    <div class="card-price">$XXXX</div>
    <ul class="card-list"><li>Artwork Printing</li><li>Vehicle Placement</li><li>Directory Listing</li></ul>
    <svg class="card-corner" width="96" height="82"><polygon points="96,0 96,82 0,82" fill="#6b8799"/></svg>
    <div class="card-go">GO</div>
  </div>
</section>

<footer>
  <div class="abs footer"></div>
  <div class="abs footer-link" style="left:217px;top:781px">How it works</div>
  <div class="abs footer-link" style="left:217px;top:813px">Post an Ad</div>
  <div class="abs footer-link" style="left:374px;top:781px">Login</div>
  <div class="abs footer-link" style="left:374px;top:813px">Contact Us</div>
  <div class="abs footer-link" style="left:530px;top:781px">Resource Centre</div>
  <div class="abs footer-link" style="left:530px;top:813px">Asia Link</div>
  <div class="abs footer-link" style="left:718px;top:781px">Terms &amp; Conditions</div>
  <div class="abs footer-link" style="left:718px;top:813px">Privacy</div>
  <div class="abs social" style="left:910px" role="img" aria-label="Social network link"></div>
  <div class="abs social" style="left:960px" role="img" aria-label="Social network link"></div>
  <div class="abs legal">© Tidewater Enterprise Assist Group 2012. Use of this website constitutes acceptance of our Terms and Conditions and Privacy Policy.</div>
</footer>

</body>
</html>
```